We need a web page design for a new company called "Quarry". We provide an innovative music sharing mobile application that allows music listeners to share their music without paying for a monthly subscription. We would like to incorporate the attached logo and color scheme. The final design should communicate music gifting and sharing.

Industry/Entity Type

It Company

```html
<!DOCTYPE html>
<html lang="en">
<head>
<meta charset="utf-8">
<title>Quarry — share the music</title>
<link href="https://fonts.googleapis.com/css2?family=Ubuntu:wght@300;400;500;700&display=swap" rel="stylesheet">
<style>
:root{
  --green:#6bb51a;
  --green-dark:#58a00c;
  --green-light:#7cc41f;
  --ink:#333333;
  --muted:#9a9a9a;
  --row-grey:#e3e3e3;
  --footer:#333333;
  --footer-line:#4a4a4a;
  --white:#ffffff;
  --charcoal:#2e2e2e;
}
*{margin:0;padding:0;box-sizing:border-box}
html,body{width:1200px;height:2625px;overflow:hidden}
body{font-family:"Ubuntu",Arial,sans-serif;background:var(--white);color:var(--ink);position:relative}
.abs{position:absolute}

/* hero */
.hero{position:absolute;left:0;top:0;width:1200px;height:816px;background:radial-gradient(ellipse at 50% 30%,var(--green-light),var(--green) 70%)}
.brand{left:188px;top:20px;display:flex;align-items:center;gap:10px;color:var(--white)}
.brand-dot{width:34px;height:34px;border-radius:50%;background:var(--white)}
.brand-name{font-size:36px;font-weight:500;line-height:1}
.brand-tag{position:absolute;left:44px;top:38px;font-size:10px;letter-spacing:1px;color:#e6f5d0;white-space:nowrap}
.nav a{position:absolute;top:30px;font-size:13px;font-weight:500;color:var(--white);text-decoration:none;letter-spacing:.3px}
.store-badge{top:22px;height:34px;border-radius:4px;background:#1d1d1d;border:1px solid #777}
.hero-rule{left:188px;top:79px;width:824px;height:1px;background:rgba(255,255,255,.3)}
.hero-title{left:0;width:1200px;top:120px;text-align:center;color:var(--white);font-size:28px;font-weight:400;letter-spacing:.5px}
.hero-sub{left:0;width:1200px;top:156px;text-align:center;color:#eaf6da;font-size:11px}
.btn-dark{left:525px;top:195px;width:154px;height:36px;background:#3a3a3a;color:var(--white);font-size:14px;font-weight:500;display:flex;align-items:center;justify-content:center;letter-spacing:.5px}
.phone-shot{top:285px;width:240px;height:480px;border-radius:30px}

/* section heads */
.section-title{left:0;width:1200px;text-align:center;font-size:26px;font-weight:300;color:#444;letter-spacing:.5px}
.section-sub{left:0;width:1200px;text-align:center;font-size:11px;color:#aaa}
.rule{left:188px;width:824px;height:1px;background:#e4e4e4}

/* features */
.device-shot{left:319px;top:938px;width:562px;height:318px;border-radius:14px}
.feature{top:1303px;width:146px;text-align:center}
.feature-tile{width:146px;height:146px;border-radius:8px;background:linear-gradient(135deg,var(--green) 50%,var(--green-dark) 50%);display:flex;align-items:center;justify-content:center}
.feature-label{margin-top:20px;font-size:12px;color:#444;white-space:nowrap;width:200px;margin-left:-27px}

/* how it works */
.tab{top:1641px;height:33px;color:var(--white);font-size:14px;font-weight:500;display:flex;align-items:center;justify-content:center;letter-spacing:.5px}
.tab-listen{left:478px;width:156px;background:var(--green);border-bottom:2px solid var(--green-dark)}
.tab-gift{left:643px;width:77px;background:var(--charcoal)}
.activity{left:188px;width:824px;height:103px}
.activity.alt{background:var(--row-grey)}
.activity-ring{position:absolute;left:14px;top:16px;width:72px;height:72px;border-radius:50%;border:20px solid var(--charcoal);background:var(--white)}
.alt .activity-ring{border-color:var(--green)}
.activity-name{position:absolute;left:103px;top:26px;font-size:26px;font-weight:500;color:#222}
.alt .activity-name{color:var(--green)}
.activity-time{position:absolute;left:103px;top:61px;font-size:11px;color:#999}
.activity-split{position:absolute;left:695px;top:10px;width:1px;height:83px;background:#cfcfcf}
.activity-dur{position:absolute;left:725px;top:36px;font-size:24px;font-weight:300;color:#333}

/* newsletter */
.signup-field{left:248px;top:2271px;width:601px;height:52px;background:#e8e8e8;font-size:11px;color:#666;padding-left:20px;display:flex;align-items:center}
.signup-send{left:849px;top:2271px;width:102px;height:52px;background:var(--green);color:var(--white);font-size:17px;font-weight:500;display:flex;align-items:center;justify-content:center}

/* footer */
.footer{left:0;top:2366px;width:1200px;height:259px;background:var(--footer);color:#ccc}
.footer-note{left:0;width:1200px;top:43px;text-align:center;font-size:14px;color:#999}
.footer-rule{left:188px;top:96px;width:824px;height:1px;background:var(--footer-line)}
.footer-mail{left:188px;top:145px;font-size:14px;color:#e5e5e5}
.social{top:133px;width:42px;height:42px;border-radius:50%;background:#555}
.footer-links{right:188px;top:145px;font-size:14px;color:#e5e5e5;word-spacing:3px}
.copyright{left:0;width:1200px;top:203px;text-align:center;font-size:10px;color:#ddd}
</style>
</head>
<body>

<header class="hero">
  <div class="abs brand">
    <span class="brand-dot"></span>
    <span class="brand-name">Quarry</span>
    <span class="brand-tag">share the music</span>
  </div>
  <nav class="nav">
    <a style="left:444px">KEY VALUES</a>
    <a style="left:536px">MOBILE APP FEATURES</a>
    <a style="left:688px">HOW IT WORKS</a>
  </nav>
  <div class="abs store-badge" style="left:802px;width:100px"></div>
  <div class="abs store-badge" style="left:913px;width:99px"></div>
  <div class="abs hero-rule"></div>
  <h1 class="abs hero-title">AN APP TO VISUALIZE YOUR DAILY ACTIVITIES</h1>
  <p class="abs hero-sub">an innovative music sharing mobile application that allows music listeners to share their music without paying for a monthly subscription.</p>
  <div class="abs btn-dark">DOWNLOAD APPS</div>
  <div class="abs phone-shot" style="left:206px;background:linear-gradient(180deg,#2a2a2a 0%,#3bb7d8 18%,#f2d64a 60%,#2a2a2a 100%)" role="img" aria-label="Phone showing the app home screen with category tiles"></div>
  <div class="abs phone-shot" style="left:478px;background:linear-gradient(180deg,#2a2a2a 0%,#2fd3a8 20%,#1bb8d2 45%,#f4f4f4 70%,#2a2a2a 100%)" role="img" aria-label="Phone showing a food and drink quiz question"></div>
  <div class="abs phone-shot" style="left:752px;background:linear-gradient(180deg,#2a2a2a 0%,#48d8f0 20%,#c9e8ef 55%,#1aa6d6 80%,#2a2a2a 100%)" role="img" aria-label="Phone showing a history topic illustration"></div>
</header>

<section>
  <h2 class="abs section-title" style="top:852px">MOBILE APP FEATURES</h2>
  <p class="abs section-sub" style="top:886px">an innovative music sharing mobile application that allows music listeners to share their music without paying for a monthly subscription.</p>
  <div class="abs device-shot" style="background:linear-gradient(90deg,#f0f0f0 0%,#e6e6e6 25%,#1e1e1e 35%,#2a2a2a 55%,#f2f2f2 65%,#e8e8e8 80%,#1e1e1e 95%)" role="img" aria-label="Group of smartphones displaying analytics charts"></div>

  <div class="abs feature" style="left:188px">
    <div class="feature-tile">
      <svg width="70" height="70" viewBox="0 0 70 70" fill="none" stroke="#fff" stroke-width="5"><circle cx="35" cy="35" r="29"/><line x1="14" y1="56" x2="56" y2="14"/><text x="35" y="48" text-anchor="middle" font-family="Ubuntu,sans-serif" font-size="38" font-weight="700" fill="#fff" stroke="none">$</text></svg>
    </div>
    <p class="feature-label">NO MONTHLY FEES</p>
  </div>
  <div class="abs feature" style="left:357px">
    <div class="feature-tile">
      <svg width="70" height="70" viewBox="0 0 70 70" fill="#fff"><path d="M35 36 C20 24 22 10 31 12 C34 13 35 16 35 16 C35 16 36 13 39 12 C48 10 50 24 35 36Z"/><path d="M8 44 h12 l10 6 h16 a4 4 0 0 1 0 8 H30 v2 h18 l14-10 a4 4 0 0 1 5 5 L50 64 H8Z"/></svg>
    </div>
    <p class="feature-label">SHARE YOUR FAVOURITE</p>
  </div>
  <div class="abs feature" style="left:527px">
    <div class="feature-tile">
      <svg width="70" height="70" viewBox="0 0 70 70" fill="none" stroke="#fff" stroke-width="4"><rect x="10" y="24" width="50" height="12"/><rect x="14" y="36" width="42" height="26"/><line x1="35" y1="24" x2="35" y2="62"/><path d="M35 24 C28 10 16 14 24 22 M35 24 C42 10 54 14 46 22"/></svg>
    </div>
    <p class="feature-label">SEND MUSIC GIFT</p>
  </div>
  <div class="abs feature" style="left:696px">
    <div class="feature-tile">
      <svg width="70" height="70" viewBox="0 0 70 70" fill="#fff"><rect x="8" y="12" width="30" height="5"/><rect x="8" y="24" width="24" height="5"/><rect x="8" y="36" width="20" height="5"/><rect x="40" y="12" width="5" height="40"/><path d="M45 12 q14 6 14 18 q-4-8-14-8Z"/><circle cx="36" cy="52" r="10"/></svg>
    </div>
    <p class="feature-label">CREATE PLAYLIST</p>
  </div>
  <div class="abs feature" style="left:864px">
    <div class="feature-tile">
      <svg width="70" height="70" viewBox="0 0 70 70" fill="#fff"><rect x="16" y="8" width="36" height="50"/><circle cx="52" cy="54" r="11" fill="#58a00c"/><rect x="50" y="46" width="4" height="16"/><rect x="44" y="52" width="16" height="4"/></svg>
    </div>
    <p class="feature-label">NEW ALBUMS</p>
  </div>

  <div class="abs rule" style="top:1521px"></div>
</section>

<section>
  <h2 class="abs section-title" style="top:1557px">HOW IT WORKS</h2>
  <p class="abs section-sub" style="top:1591px">an innovative music sharing mobile application that allows music listeners to share their music without paying for a monthly subscription.</p>
  <div class="abs tab tab-listen">SELECT LISTEN</div>
  <div class="abs tab tab-gift">GIFT</div>

  <div class="abs activity alt" style="top:1710px"><span class="activity-ring"></span><span class="activity-name">Music</span><span class="activity-time">9:00 AM - 12:23 AM</span><span class="activity-split"></span><span class="activity-dur">03:23</span></div>
  <div class="abs activity" style="top:1813px"><span class="activity-ring"></span><span class="activity-name">Chilling</span><span class="activity-time">9:00 AM - 12:23 AM</span><span class="activity-split"></span><span class="activity-dur">02:15</span></div>
  <div class="abs activity alt" style="top:1916px"><span class="activity-ring"></span><span class="activity-name">Working</span><span class="activity-time">9:00 AM - 12:23 AM</span><span class="activity-split"></span><span class="activity-dur">03:23</span></div>
  <div class="abs activity" style="top:2019px"><span class="activity-ring"></span><span class="activity-name">Transport</span><span class="activity-time">9:00 AM - 12:23 AM</span><span class="activity-split"></span><span class="activity-dur">01:35</span></div>

  <div class="abs rule" style="top:2151px"></div>
</section>

<section>
  <h2 class="abs section-title" style="top:2188px">NEWSLETTER SIGNUP</h2>
  <p class="abs section-sub" style="top:2222px">It's the best way to experience your wedding with your guests</p>
  <div class="abs signup-field">Enter phone number or email</div>
  <div class="abs signup-send">SEND</div>
</section>

<footer class="abs footer">
  <p class="abs footer-note">Tell us what device you're using and we'll add it to our todo list</p>
  <div class="abs footer-rule"></div>
  <p class="abs footer-mail">MAIL US: hello@quarry.com</p>
  <span class="abs social" style="left:523px"></span>
  <span class="abs social" style="left:573px"></span>
  <span class="abs social" style="left:626px"></span>
  <p class="abs footer-links">JOBS | FAQ | PRIVACY &amp; TERMS</p>
  <p class="abs copyright">© COPYRIGHT 2014 · ALL RIGHTS RESERVED</p>
</footer>

</body>
</html>
```